Educational Construction Organization needs Flyer for Upcoming Forum

We need a SAVE THE DATE Flyer for our 2020 Ravteq Forum. We work with Architects, Engineers, Contractors and Owners in the design and construction industry. Our mission is to evolve the capital projects industry through sharing of knowledge for optimized leadership, delivery and performance. The final design should communicate the connection between these industry professionals, our mission, and the Forum theme and byline.
Updates

Need extra days to review

Target Market(s)

Design and construction industry.

Industry/Entity Type

Construction

Font styles to use
Sans Serif

Colors

Designer to choose colors to be used in the design.

Requirements
Must have
• Title, By-line, 3 key topics, Date and location. Design that implements the theme with graphic(s) (not just text).
• NEW TITLE: FUTURE PROOFING: Connecting the dots to make sense of the "SMART" City
• 3 Key Topics: Smart Cities, Smart Institutions, Smart Connections
• Date: April 1-3, 2020
• Location: San Antonio, TX
Nice to have
• Please review attached problem statement for a better understanding of what this Forum will focus on when designing your graphic for the flyer.

```html
<!DOCTYPE html>
<html lang="en">
<head>
<meta charset="utf-8">
<title>Save the Date – Future Proofing: Making Sense of the Smart City</title>
<link rel="stylesheet" href="https://fonts.googleapis.com/css2?family=Montserrat:wght@400;500;600;700&family=Roboto+Condensed:wght@400;700&family=Open+Sans:wght@400&display=swap">
<style>
  :root {
    --page-bg: #eeeeee;
    --paper: #ffffff;
    --slate: #5a5a5a;
    --navy: #2e3d8a;
    --lime: #8cb030;
    --ink: #3a3a3a;
    --text-grey: #444444;
    --rule: #6a6a6a;
  }
  * { margin: 0; padding: 0; box-sizing: border-box; }
  html, body {
    width: 1200px; height: 799px; overflow: hidden;
    background: var(--page-bg);
  }
  .flyer-stage {
    position: absolute; left: 329px; top: 14px;
    width: 542px; height: 770px;
  }
  .flyer {
    position: relative; width: 605px; height: 860px;
    background: var(--paper);
    overflow: hidden;
    transform: scale(0.8959); transform-origin: 0 0;
    box-shadow: 0 4px 14px rgba(0,0,0,0.12);
  }
  .flyer-shapes { position: absolute; inset: 0; }

  .brand {
    position: absolute; left: 49px; top: 40px;
    display: flex; align-items: center; gap: 14px;
  }
  .brand-dot { width: 60px; height: 60px; border-radius: 50%; background: var(--navy); }
  .brand-name {
    font-family: "Montserrat", sans-serif; font-weight: 500;
    font-size: 40px; color: var(--ink); letter-spacing: 0.5px;
  }

  .date-block {
    position: absolute; right: 28px; top: 155px;
    text-align: right; color: var(--paper);
  }
  .save {
    font-family: "Roboto Condensed", sans-serif; font-weight: 700;
    font-size: 96px; line-height: 0.9; letter-spacing: -1px;
  }
  .the-date {
    font-family: "Montserrat", sans-serif; font-weight: 400;
    font-size: 31px; line-height: 1.2; margin-top: 2px;
  }
  .dates {
    position: absolute; left: 425px; top: 292px; width: 170px;
    text-align: center; color: var(--paper);
    font-family: "Roboto Condensed", sans-serif; font-weight: 700;
    font-size: 36px; line-height: 42px;
  }
  .dates sup { font-size: 16px; vertical-align: 14px; }
  .dates .year { color: var(--lime); font-size: 58px; line-height: 64px; }
  .dates .location {
    font-family: "Montserrat", sans-serif; font-weight: 500;
    font-size: 17px; line-height: 24px; margin-top: 2px;
  }

  .kicker {
    position: absolute; left: 33px; top: 528px;
    font-family: "Montserrat", sans-serif; font-weight: 700;
    font-size: 19px; letter-spacing: 3px; color: var(--slate);
  }
  .title {
    position: absolute; left: 33px; top: 562px;
    font-family: "Roboto Condensed", sans-serif; font-weight: 700;
    font-size: 53px; line-height: 50px; text-transform: uppercase;
  }
  .title-top { color: var(--navy); display: block; }
  .title-bottom { color: var(--lime); display: block; }

  .byline {
    position: absolute; left: 33px; top: 677px; width: 420px;
    font-family: "Open Sans", sans-serif; font-size: 18.5px;
    line-height: 24px; color: var(--text-grey);
  }
  .divider {
    position: absolute; left: 28px; top: 742px; width: 424px; height: 2px;
    background: linear-gradient(90deg, rgba(90,90,90,0.2), var(--rule) 30%, var(--rule) 70%, rgba(90,90,90,0.2));
  }
  .topics {
    position: absolute; left: 33px; top: 760px;
    display: flex; align-items: center; gap: 18px;
  }
  .topics-word {
    font-family: "Montserrat", sans-serif; font-weight: 700;
    font-size: 72px; line-height: 1; color: var(--navy); letter-spacing: -1px;
  }
  .topics-list {
    list-style: none;
    font-family: "Montserrat", sans-serif; font-weight: 400;
    font-size: 16.5px; line-height: 23px; color: var(--text-grey);
  }
</style>
</head>
<body>
  <div class="flyer-stage">
    <article class="flyer">
      <svg class="flyer-shapes" width="605" height="860" viewBox="0 0 605 860">
        <defs>
          <linearGradient id="meeting-tones" x1="0" y1="0" x2="0" y2="1">
            <stop offset="0" stop-color="#e4e8ec"/>
            <stop offset="0.45" stop-color="#b7c0c8"/>
            <stop offset="0.7" stop-color="#8a6a52"/>
            <stop offset="1" stop-color="#b07a4e"/>
          </linearGradient>
        </defs>
        <circle class="slate-disc" cx="593" cy="290" r="290" fill="var(--slate)"/>
        <circle class="meeting-photo" cx="168" cy="318" r="188" fill="url(#meeting-tones)"
                role="img" aria-label="Photo of professionals meeting around a conference table with laptops"/>
        <circle class="lime-disc" cx="316" cy="455" r="80" fill="var(--lime)"/>
        <circle class="navy-disc" cx="606" cy="648" r="123" fill="var(--navy)"/>
      </svg>

      <header class="brand">
        <span class="brand-dot"></span>
        <span class="brand-name">I-Ravteq</span>
      </header>

      <div class="date-block">
        <div class="save">SAVE</div>
        <div class="the-date">THE DATE</div>
      </div>
      <div class="dates">
        <div>1<sup>st</sup> April</div>
        <div>to</div>
        <div>3<sup>rd</sup> April,</div>
        <div class="year">2020</div>
        <div class="location">San Antonio, TX</div>
      </div>

      <p class="kicker">FUTURE PROOFING:</p>
      <h1 class="title">
        <span class="title-top">Making Sense of</span>
        <span class="title-bottom">The Smart City</span>
      </h1>
      <p class="byline">Connecting the Dots for Dynamic Planning, Design and Delivery</p>
      <div class="divider"></div>
      <div class="topics">
        <span class="topics-word">SMART</span>
        <ul class="topics-list">
          <li>CITIES</li>
          <li>INSTITUTIONS</li>
          <li>CONNECTIONS</li>
        </ul>
      </div>
    </article>
  </div>
</body>
</html>
```